Website Redesign using existing images, copy etc.

I'm looking for a website redesign/refresh of my current WordPress website. I would like to utilize the same photography, a new photo viewer, and an overall refresh of the entire design. This will need to be WordPress with simple accessibility to make changes as we add additional properties and make updates. We auction luxury real estate and luxury yachts for non-distressed sellers. It needs to be simple, luxurious and with ease of use for both web and especially mobile. www.HarborCrestBids.com

```html
<!DOCTYPE html>
<html lang="en">
<head>
<meta charset="utf-8">
<title>Harbor Crest — Real Estate &amp; Yachts</title>
<link rel="stylesheet" href="https://fonts.googleapis.com/css2?family=Tenor+Sans&family=Montserrat:wght@400;500;600;700&display=swap">
<style>
:root{
  --gold:#a8956b;
  --sand:#cbbfa6;
  --navy:#1c2533;
  --ink:#2a2a2a;
  --body:#444;
  --white:#fff;
  --footer:#1f1f1f;
  --footer-box:#2a2a2a;
}
*{margin:0;padding:0;box-sizing:border-box}
html,body{width:1200px;height:4926px;overflow:hidden}
body{position:relative;background:var(--white);font-family:"Montserrat",sans-serif;color:var(--body)}
.abs{position:absolute}
.display{font-family:"Tenor Sans",sans-serif;font-weight:400;color:var(--ink);text-transform:uppercase;letter-spacing:-0.5px}
.btn{position:absolute;display:flex;align-items:center;justify-content:center;gap:12px;font-size:8px;font-weight:700;letter-spacing:3px;text-transform:uppercase;color:var(--white);white-space:nowrap}
.btn svg{width:22px;height:8px}
.btn--gold{background:var(--gold)}
.btn--navy{background:var(--navy)}
.btn--white{background:var(--white);color:var(--ink)}
.copy{font-size:13.5px;line-height:29px;color:var(--body)}

/* hero */
.hero{left:0;top:0;width:1200px;height:782px;background:linear-gradient(180deg,#7fb6e0 0%,#a9cbe3 30%,#e8c9a0 55%,#8aa7b8 72%,#2d7fb8 86%,#4fa6d6 100%)}
.topbar{font-size:10px;color:var(--white);display:flex;align-items:center;gap:12px}
.topbar svg{width:20px;height:20px}
.nav-line{height:1px;background:rgba(255,255,255,.7)}
.nav-link{font-size:10px;font-weight:500;letter-spacing:1px;color:var(--white);text-transform:uppercase}
.nav-name{left:540px;top:58px;width:120px;text-align:center;font-family:"Tenor Sans",sans-serif;font-size:13px;line-height:16px;letter-spacing:2px;color:var(--white)}
.hero-title{left:0;width:1200px;text-align:center;font-family:"Tenor Sans",sans-serif;text-transform:uppercase;line-height:1}
.hero-card{left:277px;top:523px;width:644px;height:160px;background:var(--white)}

/* photo blocks */
.photo{position:absolute}
.yacht-day{background:linear-gradient(180deg,#b9d3ea 0%,#dfe9f1 45%,#2f5e8c 62%,#173c66 100%)}
.villa{background:linear-gradient(180deg,#c79a8e 0%,#b9a08a 25%,#3e4a30 60%,#7a5a48 100%)}
.yacht-dock{background:linear-gradient(180deg,#6aa0d6 0%,#9ec5e6 50%,#1b2a45 62%,#5d8fb8 100%)}
.aerial{background:linear-gradient(180deg,#a9c7e0 0%,#4e7fa3 35%,#567a3c 65%,#3e5a2c 100%)}
.skyline{background:linear-gradient(180deg,#d8b6a8 0%,#e6c6a6 40%,#9fa2a8 65%,#3d4a5a 100%)}
.tower{background:linear-gradient(160deg,#1d3f8a 0%,#2a5bb3 45%,#0f2553 100%)}

/* press */
.press{left:522px;top:1189px;width:678px;height:549px;background:var(--sand)}
.press-cell{position:absolute;width:159px;height:104px;display:flex;align-items:center;justify-content:center;text-align:center;font-family:"Tenor Sans",sans-serif;color:#4a4a4a;font-size:15px;line-height:18px}
.press-cell--lit{background:rgba(255,255,255,.18)}

/* slider */
.arrow{width:26px;height:26px}
.sold-card{left:157px;top:2425px;width:886px;height:209px;background:var(--white);box-shadow:0 4px 14px rgba(0,0,0,.08);text-align:center}

/* split */
.split-title{font-family:"Tenor Sans",sans-serif;color:var(--white);font-size:40px;text-transform:uppercase;width:600px;text-align:center}

/* footer */
.footer{left:0;top:4379px;width:1200px;height:547px;background:var(--footer);color:#ddd}
.f-head{font-family:"Tenor Sans",sans-serif;font-size:14px;color:#ddd;text-transform:uppercase}
.f-link{font-size:10.5px;color:#ccc;line-height:26px}
.social{width:30px;height:30px;border-radius:50%}
.field{width:256px;height:25px;background:var(--white);font-size:7px;letter-spacing:1px;color:#555;padding:8px 20px}
.f-small{font-size:9.5px;color:#ccc}
</style>
</head>
<body>

<!-- HERO -->
<section class="abs hero" role="img" aria-label="Waterfront skyline of luxury high-rise towers reflected in a marina at sunrise"></section>
<div class="abs topbar" style="left:322px;top:8px"><svg viewBox="0 0 20 20"><circle cx="10" cy="10" r="10" fill="#1a1a1a"/><path d="M7 5.5l2 2-1 1.2a6 6 0 0 0 3.3 3.3l1.2-1 2 2-1.3 1.5C9.5 14 6 10.5 5.5 6.8z" fill="#fff"/></svg>855-210-4471</div>
<div class="abs topbar" style="left:796px;top:8px"><svg viewBox="0 0 20 20"><circle cx="10" cy="10" r="10" fill="#1a1a1a"/><rect x="5.5" y="6.5" width="9" height="7" fill="#fff"/><path d="M5.5 6.5l4.5 4 4.5-4" stroke="#1a1a1a" fill="none"/></svg>hello@harborcrestbids.com</div>
<div class="abs nav-line" style="left:249px;top:44px;width:283px"></div>
<div class="abs nav-line" style="left:666px;top:44px;width:311px"></div>
<div class="abs nav-line" style="left:249px;top:92px;width:283px"></div>
<div class="abs nav-line" style="left:666px;top:92px;width:311px"></div>
<a class="abs nav-link" style="left:326px;top:61px">Buy</a>
<span class="abs" style="left:389px;top:65px;width:5px;height:5px;border-radius:50%;background:var(--gold)"></span>
<a class="abs nav-link" style="left:435px;top:61px">Sell</a>
<a class="abs nav-link" style="left:738px;top:61px">About</a>
<a class="btn btn--gold" style="left:827px;top:53px;width:121px;height:28px">Contact<svg viewBox="0 0 22 8"><path d="M0 4h20M17 1l3 3-3 3" stroke="#fff" fill="none"/></svg></a>
<div class="abs nav-name">HARBOR<br>CREST</div>

<h1 class="abs hero-title" style="top:160px;font-size:88px;color:var(--white)">Harbor</h1>
<div class="abs hero-title" style="top:258px;font-size:96px;color:#e7c98a">Crest</div>

<div class="abs hero-card"></div>
<div class="abs display" style="left:277px;top:548px;width:644px;text-align:center;font-size:23px">Real Estate &amp; Yachts</div>
<a class="btn btn--gold" style="left:335px;top:591px;width:258px;height:29px">Browse upcoming auctions<svg viewBox="0 0 22 8"><path d="M0 4h20M17 1l3 3-3 3" stroke="#fff" fill="none"/></svg></a>
<a class="btn btn--navy" style="left:603px;top:591px;width:260px;height:29px">Browse past successes<svg viewBox="0 0 22 8"><path d="M0 4h20M17 1l3 3-3 3" stroke="#fff" fill="none"/></svg></a>
<svg class="abs" style="left:556px;top:633px" width="88" height="88" viewBox="0 0 88 88" aria-label="Watch our video">
  <defs><path id="ring" d="M44 44m-36 0a36 36 0 1 1 72 0"/></defs>
  <circle cx="44" cy="44" r="40" fill="#fff"/>
  <text font-family="Montserrat,sans-serif" font-size="7.5" font-weight="700" letter-spacing="2" fill="#2a2a2a"><textPath href="#ring" startOffset="14%">WATCH OUR VIDEO</textPath></text>
  <circle cx="44" cy="44" r="22" fill="#a8956b"/>
  <path d="M40 36l11 8-11 8z" fill="#fff"/>
</svg>
<div class="abs" style="left:599px;top:727px;width:1px;height:102px;background:#bbb"></div>

<!-- INTRO -->
<h2 class="abs display" style="left:197px;top:880px;font-size:44px;line-height:46px">Over one billion<br>dollars of auctions<br>marketed</h2>
<div class="abs" style="left:197px;top:1036px;font-size:12px;font-weight:700;letter-spacing:4.5px;color:var(--gold)">REAL ESTATE &amp; YACHTS</div>
<p class="abs copy" style="left:522px;top:998px;width:490px">The experience of hearing the auctioneer’s final proclamation of “SOLD!” is unparalleled. Whether it’s the initial meeting with the seller at their estate or yacht, or the triumphant raising of the paddle by the winning buyer, we relish every moment of the process and the ensuing festivities. We’re confident that you will, too.</p>

<div class="photo yacht-day" style="left:0;top:1095px;width:471px;height:522px" role="img" aria-label="White superyacht cruising on deep blue open water"></div>

<section class="abs press">
  <h2 class="abs display" style="left:0;top:66px;width:678px;text-align:center;font-size:40px">As featured in</h2>
  <div class="press-cell press-cell--lit" style="left:100px;top:132px">The Ledger<br>Daily</div>
  <div class="press-cell" style="left:259px;top:132px;font-size:20px">Capital Weekly</div>
  <div class="press-cell" style="left:420px;top:132px;font-size:11px">ESTATE QUARTERLY</div>
  <div class="press-cell" style="left:100px;top:237px;font-size:18px">Market Hour</div>
  <div class="press-cell" style="left:259px;top:237px;font-size:13px">Evening Wire</div>
  <div class="abs" style="left:259px;top:142px;width:1px;height:190px;background:rgba(255,255,255,.5)"></div>
  <div class="abs" style="left:420px;top:142px;width:1px;height:84px;background:rgba(255,255,255,.5)"></div>
  <div class="abs" style="left:110px;top:237px;width:470px;height:1px;background:rgba(255,255,255,.5)"></div>
  <p class="abs" style="left:100px;top:370px;width:478px;text-align:center;font-size:10px;line-height:21px;color:#5a5244">By offering top-tier properties and vessels globally, along with strategic auction dates, exceptional marketing tactics, and a diligent public relations team, even the most prominent media outlets have taken notice. Check out some of our latest press features.</p>
  <a class="btn btn--navy" style="left:268px;top:461px;width:144px;height:29px">View press<svg viewBox="0 0 22 8"><path d="M0 4h20M17 1l3 3-3 3" stroke="#fff" fill="none"/></svg></a>
</section>

<div class="abs" style="left:197px;top:1712px;font-family:'Tenor Sans',sans-serif;font-size:26px;line-height:32px;letter-spacing:4px;color:var(--gold)">HARBOR<br>CREST</div>

<!-- SLIDER -->
<div class="photo villa" style="left:71px;top:1874px;width:1058px;height:649px" role="img" aria-label="Mediterranean-style waterfront villa at dusk with palm trees and a brick-paved drive"></div>
<svg class="abs arrow" style="left:6px;top:2184px" viewBox="0 0 26 26"><path d="M16 6l-7 7 7 7" stroke="#333" stroke-width="2" fill="none"/></svg>
<svg class="abs arrow" style="left:1168px;top:2218px" viewBox="0 0 26 26"><path d="M10 6l7 7-7 7" stroke="#333" stroke-width="2" fill="none"/></svg>
<div class="abs sold-card">
  <div class="display" style="margin-top:32px;font-size:40px;line-height:46px">Sold<br>by Harbor Crest</div>
  <div style="margin-top:16px;font-size:19px;color:var(--ink)">Naples | Florida</div>
</div>
<a class="btn btn--gold" style="left:494px;top:2618px;width:210px;height:27px">View success story<svg viewBox="0 0 22 8"><path d="M0 4h20M17 1l3 3-3 3" stroke="#fff" fill="none"/></svg></a>

<!-- ABOUT COPY -->
<p class="abs copy" style="left:197px;top:2792px;width:340px">Harbor Crest is a top-tier destination for luxury property auctions, having overseen the auction marketing of numerous high-end estates and yachts. Our team of luxury home auction experts is committed to helping property owners obtain the best value for their assets while ensuring a timely sale. Whether you have an expansive compound or a metropolitan penthouse, Harbor Crest has the necessary skills and expertise to facilitate various luxury real estate auctions.</p>
<div class="photo yacht-dock" style="left:609px;top:2750px;width:394px;height:408px" role="img" aria-label="Navy-hulled motor yacht moored at a marina under blue sky"></div>
<div class="photo aerial" style="left:197px;top:3160px;width:412px;height:452px" role="img" aria-label="Aerial view of a waterfront estate surrounded by trees on a peninsula"></div>
<p class="abs copy" style="left:656px;top:3206px;width:346px">What’s even better? Our team takes care of every aspect of the process in cooperation with your realtor/broker, including property tours, photography and cinematography, marketing advertising, public relations and more. Apart from high-end real estate auctions, we can also organize and execute luxury yacht auctions to help boat owners find qualified buyers for their vessels. Interested in finding out more about our luxury home and yacht auctions? Explore our current listings and success stories!</p>
<a class="btn btn--navy" style="left:656px;top:3549px;width:236px;height:30px">View all success story<svg viewBox="0 0 22 8"><path d="M0 4h20M17 1l3 3-3 3" stroke="#fff" fill="none"/></svg></a>

<!-- SPLIT -->
<div class="photo skyline" style="left:0;top:3729px;width:600px;height:650px" role="img" aria-label="Yacht cruising past a city skyline at sunset"></div>
<div class="photo tower" style="left:600px;top:3729px;width:600px;height:650px" role="img" aria-label="Blue glass skyscraper viewed from below"></div>
<h2 class="abs split-title" style="left:0;top:4005px">About us</h2>
<a class="btn btn--gold" style="left:228px;top:4078px;width:145px;height:28px">Learn more<svg viewBox="0 0 22 8"><path d="M0 4h20M17 1l3 3-3 3" stroke="#fff" fill="none"/></svg></a>
<h2 class="abs split-title" style="left:600px;top:4005px">Upcoming auctions</h2>
<a class="btn btn--white" style="left:828px;top:4078px;width:145px;height:28px">Browse<svg viewBox="0 0 22 8"><path d="M0 4h20M17 1l3 3-3 3" stroke="#333" fill="none"/></svg></a>

<!-- FOOTER -->
<footer class="abs footer">
  <div class="abs" style="left:197px;top:119px;width:207px;height:1px;background:#666"></div>
  <div class="abs" style="left:796px;top:119px;width:207px;height:1px;background:#666"></div>
  <div class="abs" style="left:420px;top:104px;width:360px;text-align:center;font-family:'Tenor Sans',sans-serif;font-size:24px;letter-spacing:6px;color:#eee">HARBOR CREST</div>

  <div class="abs f-head" style="left:197px;top:218px">Follow along</div>
  <div class="abs" style="left:197px;top:263px;display:flex;gap:14px">
    <span class="social" style="background:#3b5ba5" aria-label="Social profile 1"></span>
    <span class="social" style="background:#c13584" aria-label="Social profile 2"></span>
    <span class="social" style="background:#1da1f2" aria-label="Social profile 3"></span>
    <span class="social" style="background:#0a66c2" aria-label="Social profile 4"></span>
  </div>
  <div class="abs" style="left:200px;top:357px;width:52px;height:52px;border-radius:50%;background:#555" aria-label="Partner badge"></div>

  <div class="abs" style="left:402px;top:206px;width:1px;height:220px;background:#555"></div>
  <div class="abs f-head" style="left:454px;top:218px">Quick links</div>
  <ul class="abs" style="left:454px;top:252px;list-style:none">
    <li class="f-link">Home</li><li class="f-link">Buy</li><li class="f-link">Sell</li><li class="f-link">About</li><li class="f-link">Blog</li><li class="f-link">Contact</li>
  </ul>
  <div class="abs" style="left:605px;top:206px;width:1px;height:220px;background:#555"></div>

  <div class="abs" style="left:651px;top:215px;width:317px;height:214px;background:var(--footer-box)">
    <div class="abs f-head" style="left:31px;top:30px;font-size:13px">Sign up for Harbor Crest alerts</div>
    <div class="abs field" style="left:31px;top:68px">NAME</div>
    <div class="abs field" style="left:31px;top:105px">EMAIL</div>
    <a class="btn btn--gold" style="left:31px;top:153px;width:148px;height:30px">Submit<svg viewBox="0 0 22 8"><path d="M0 4h20M17 1l3 3-3 3" stroke="#fff" fill="none"/></svg></a>
  </div>

  <div class="abs f-small" style="left:197px;top:524px">Copyright © 2023 harbor crest. All Rights Reserved</div>
  <div class="abs f-small" style="left:683px;top:524px;display:flex;gap:32px;font-size:8.5px"><span>TERMS OF SERVICE</span><span>COPYRIGHT</span><span>POLICY PRIVACY POLICY</span></div>
</footer>

</body>
</html>
```